"Breathe & Bloom" Book Cover 5.5x8.5

Title of the book is "Breathe & Bloom"
Subtitle is "Unmasking Pricing Myths"
I've used PixelGuild on multiple occasions you can look on my Borvex page, Mark Delwitt, to see the covers I've used in the other projects I've done.
The target audience are people who have been tricked to think they can't retire because inflation, i.e. cost of living is going up so much they must work to keep up. There is no evidence of this.
And those are the people I want to reach so they can "Breathe...and Bloom."
Target Market(s)
Americans aged 55 and over who are thinking about retirement
Industry/Entity Type
Financial
Requirements
Nice to have
- Keep It Simple, Stupid is my mantra. Just make it pop out when people are browsing
Should not have
- No piggy banks. No old people sitting on a beach.

```html
<!DOCTYPE html>
<html lang="en">
<head>
<meta charset="utf-8">
<title>Breathe &amp; Bloom – Mark Delwitt</title>
<link rel="stylesheet" href="https://fonts.googleapis.com/css2?family=Noto+Sans:wght@400;700&family=Oswald:wght@700&family=Roboto:wght@400&family=Crimson+Text&family=Cinzel:wght@400;700&display=swap">
<style>
  :root {
    --page: #ffffff;
    --frame: #111111;
    --panel: #ffffff;
    --panel-head: #f3f5f5;
    --ink: #111111;
    --muted: #555555;
    --rule: #dddddd;
    --follow: #fcd54c;
    --price: #b12704;
    --amp: #9db5dc;
    --subtitle: #3f86b6;
    --author: #1c86a8;
    --royal: #2f45a8;
    --band: #3a4fb0;
  }
  * { box-sizing: border-box; margin: 0; padding: 0; }
  html, body { width: 1200px; height: 848px; overflow: hidden; background: var(--page); }
  .canvas {
    position: relative; width: 1200px; height: 848px;
    border: 1px solid var(--frame); background: var(--page); overflow: hidden;
    font-family: "Noto Sans", sans-serif;
  }
  .author-panel {
    position: absolute; left: 32px; top: 184px; width: 740px; height: 442px;
    background: var(--panel); border-top: 1px solid #999;
    box-shadow: 0 12px 14px rgba(0,0,0,.35);
  }
  .author-panel__head { position: absolute; left: 0; top: 0; width: 100%; height: 76px; background: var(--panel-head); }
  .author-name { position: absolute; left: 361px; top: 18px; font-size: 31px; font-weight: 700; color: var(--ink); letter-spacing: .2px; }
  .avatar {
    position: absolute; left: 46px; top: 24px; width: 264px; height: 264px; border-radius: 50%;
    background: radial-gradient(circle at 50% 45%, #b8705e 0 22%, #0a0a0a 23% 60%, #6f9bd6 61%);
  }
  .follow-btn {
    position: absolute; left: 46px; top: 313px; width: 265px; height: 47px; border-radius: 8px;
    background: var(--follow); color: var(--ink); font-size: 15px;
    display: flex; align-items: center; justify-content: center;
  }
  .follow-note { position: absolute; left: 46px; top: 368px; width: 270px; font-size: 15.5px; line-height: 23px; color: var(--muted); }
  .follow-rule { position: absolute; left: 46px; top: 424px; width: 265px; border-top: 1px solid var(--rule); }
  .book-tile { position: absolute; top: 106px; }
  .book-tile--one { left: 364px; }
  .book-tile--two { left: 563px; }
  .book-tile__cover { display: block; }
  .book-tile__price { position: absolute; top: 283px; left: 0; font-size: 15px; color: var(--price); white-space: nowrap; }
  .book-tile__format { position: absolute; top: 307px; left: 0; font-size: 13px; color: var(--muted); white-space: nowrap; }
  .feature-cover {
    position: absolute; left: 764px; top: 105px; width: 403px; height: 644px;
    box-shadow: 10px 10px 14px rgba(0,0,0,.45);
  }
  .feature-cover svg { display: block; }
</style>
</head>
<body>
<div class="canvas">

  <svg width="0" height="0" style="position:absolute" aria-hidden="true">
    <defs>
      <linearGradient id="coverBg" x1="0" y1="0" x2="1" y2="1">
        <stop offset="0" stop-color="#f5f8fa"/>
        <stop offset=".5" stop-color="#dfe9ef"/>
        <stop offset="1" stop-color="#c7d7e2"/>
      </linearGradient>
      <linearGradient id="titleFill" gradientUnits="userSpaceOnUse" x1="0" y1="111" x2="0" y2="614">
        <stop offset="0" stop-color="#1a86ac"/>
        <stop offset=".45" stop-color="#5a8398"/>
        <stop offset="1" stop-color="#15394a"/>
      </linearGradient>
      <symbol id="coverArt" viewBox="0 0 403 644">
        <rect width="403" height="644" fill="url(#coverBg)" role="img" aria-label="Photo of a man resting in a hammock by the sea"/>
        <text transform="translate(90,77) rotate(-35)" text-anchor="middle" dominant-baseline="central" font-family="Noto Sans, sans-serif" font-weight="700" font-size="130" fill="var(--amp)">&amp;</text>
        <text font-family="Roboto, sans-serif" font-size="18" letter-spacing="1.5" fill="var(--subtitle)">
          <tspan x="175" y="56">Unmasking</tspan>
          <tspan x="175" y="76">Pricing</tspan>
          <tspan x="175" y="96">Myths</tspan>
        </text>
        <text transform="translate(151,614) rotate(-90)" font-family="Oswald, sans-serif" font-weight="700" font-size="168" fill="url(#titleFill)" textLength="471" lengthAdjust="spacingAndGlyphs">BREATHE</text>
        <text transform="translate(298,614) rotate(-90)" font-family="Oswald, sans-serif" font-weight="700" font-size="168" fill="url(#titleFill)" textLength="503" lengthAdjust="spacingAndGlyphs">BLOOM</text>
        <text transform="translate(360,614) rotate(-90)" font-family="Crimson Text, serif" font-size="30" fill="var(--author)">Mark Delwitt</text>
      </symbol>
      <linearGradient id="seaFill" x1="0" y1="0" x2="0" y2="1">
        <stop offset="0" stop-color="#d8d6dd"/>
        <stop offset=".35" stop-color="#d9c6b0"/>
        <stop offset=".6" stop-color="#b9a9b2"/>
        <stop offset="1" stop-color="#c9803e"/>
      </linearGradient>
    </defs>
  </svg>

  <section class="author-panel">
    <div class="author-panel__head"></div>
    <h1 class="author-name">Mark Delwitt</h1>
    <div class="avatar" role="img" aria-label="Portrait of the author"></div>
    <div class="follow-btn">+ Follow</div>
    <p class="follow-note">Follow to get new release updates and improved recommendations</p>
    <div class="follow-rule"></div>

    <div class="book-tile book-tile--one">
      <svg class="book-tile__cover" width="185" height="275" viewBox="0 0 185 275" aria-label="Breathe &amp; Bloom cover">
        <rect x="0" y="0" width="6" height="275" fill="#dcd9ee"/>
        <rect x="0" y="0" width="6" height="35" fill="#c09050"/>
        <use href="#coverArt" x="6" y="0" width="179" height="275" preserveAspectRatio="none"/>
      </svg>
      <span class="book-tile__price">$5.99</span>
      <span class="book-tile__format">Ebook Edition</span>
    </div>

    <div class="book-tile book-tile--two">
      <svg class="book-tile__cover" width="175" height="276" viewBox="0 0 175 276" aria-label="You Can Thrive on Steady Income cover">
        <rect width="175" height="251" fill="url(#seaFill)" role="img" aria-label="Sunset over waves on a sandy beach"/>
        <g font-family="Cinzel, serif" fill="var(--royal)" text-anchor="middle">
          <line x1="38" y1="26" x2="58" y2="26" stroke="#555" stroke-width=".8"/>
          <line x1="117" y1="26" x2="137" y2="26" stroke="#555" stroke-width=".8"/>
          <text x="87" y="30" font-size="11" fill="#333" font-weight="700">YOU CAN</text>
          <text x="87" y="70" font-size="37" font-weight="700" textLength="150" lengthAdjust="spacingAndGlyphs">THRIVE</text>
          <line x1="40" y1="79" x2="70" y2="79" stroke="#555" stroke-width=".8"/>
          <line x1="104" y1="79" x2="134" y2="79" stroke="#555" stroke-width=".8"/>
          <text x="87" y="83" font-size="10" fill="#333" font-weight="700">ON</text>
          <text x="87" y="120" font-size="33" font-weight="700" fill="#1f2f7a" textLength="152" lengthAdjust="spacingAndGlyphs">STEADY</text>
          <text x="87" y="148" font-size="29" font-weight="700" fill="#1f2f7a" textLength="152" lengthAdjust="spacingAndGlyphs">INCOME</text>
        </g>
        <rect y="251" width="175" height="25" fill="var(--band)"/>
        <text x="87" y="268" text-anchor="middle" font-family="Cinzel, serif" font-weight="700" font-size="12" letter-spacing="2" fill="#ffffff">MARK DELWITT</text>
      </svg>
      <span class="book-tile__price">$5.99</span>
      <span class="book-tile__format">Ebook Edition</span>
    </div>
  </section>

  <div class="feature-cover">
    <svg width="403" height="644" viewBox="0 0 403 644" aria-label="Breathe &amp; Bloom book cover by Mark Delwitt">
      <use href="#coverArt" x="0" y="0" width="403" height="644"/>
    </svg>
  </div>

</div>
</body>
</html>
```